Illustration Design Project- Company Project flow chart

Kolvarn Group is a start-up Sustainable Energy Solution Company. We would like a process flow chart illustration of our Renewable Harvest Network System (RHNS).
Our RHNS concept is to have numerous large-scale farms operating throughout Costa Rica. Each farm will have three main crops: Solar fields, Jatropha, and Cash crops. There are various processes within Jatropha, resulting in 5 end products.
Each one of these crops or processes will stand on its own within our report in which the illustration is being created, however two section, the Anaerobic Digester and Solar will need a few more detailed aspects for its individual breakdown than it will have on the large combined flow chart. Attached is a pic of the detailed anaerobic digester, the intake and out-take features do not need to be on the main illustration. Also attached is an illustration of a simple solar concept we want recreated for the detailed/individual breakdown.
We would like to be clear that the final deliverables should be 3 individual illustrations files:
1. Overall Company Project flow chart with concept, and each crop, process and product being represented.
2. Anaerobic Digester (detailed)
3. Solar (detailed)
We are still finalizing the copy, however we are very close and we can change this out even after the design is done. The font and style is what is the most important at this time since all copy is one to three words.
Attached are two sample flow chart representing our RHNS. 1. a Box flow chart and 2. image flow chart. Also attached is a current flow chart commonly found on the internet representing the jatropha process. We appreciate this concept, however we feel it’s outdated and represents a small scale operation. We want this to follow KVG style as well as be representative of a commercial scale operation.
KVG is open to illustration interpretation, the images enclosed are either photos from our operation or place holders. Our images are the Jatropha Cultivation, Cash Crop, Oil Extraction & filtration, Squash. Aslo attached is a low-res png KVG logo as a place holder if you choose to incorporate our logo within your illustration. We will provide the high res logo to the winning illustrator. The Globe can either be on the side of the Kolvarn Group lettering or on top of the lettering.
If you need to have more images that represent each crop, process or product, let me know and I will post upload something, however most of the time your own research, will most likely yield a viable representation. I did also upload the line art of our squash that is on our squash box.
Our Website is www.kolvarngroup.example , below are four links to videos produced by our company (Luckily, we have an ex-filmmaker on staff) These videos highlight many aspects of RHNS as well I think you will get a feel for our company.
Current project: http://www.videohost.example/watch?v=pQ3rTm8_wxL
What is Jatropha: http://www.videohost.example/watch?v=HZ7sb-qLtyR&list=AAbq4Rk-PwdLM9Ho2cZeyiTo&index=10&feature=plcp
KVG’s Expertise: http://www.videohost.example/watch?v=5wPLuj3mXaV&list=AAbq4Rk-PwdLM9Ho2cZeyiTo&index=12&feature=plcp
VenTrak: http://www.videohost.example/watch?v=TM2Q55yRkaph&list=AAbq4Rk-PwdLM9Ho2cZeyiTo&index=24&feature=plcp
Our mission statement is:
Develop and implement solutions and technologies in the field of energy that are designed to bring social economic and environmental advancement to communities through self-sustainable green methods.
Reason: At designers requests
Thank you, please send in your designs ASAP, so we can provide feedback.
Thank you.
Oskar Lindqvist
Reason: Because of designers requests and we raised the total by $100. This is the final deadline! Thank you, I look forward to seeing your work! Thank you for your participation!
Regards,
Oskar
We have increased the budget to the wining design to $290. We also provided three participation payments. Please note the deadline for this Saturday Feb 11! at 4pm. We look forward to seeing your work.
Reason: Today will be deadline, basically 10 more hours. Reason, request by designers.
Target Market(s)
High level professionals and investors
Industry/Entity Type
Internet
Requirements
Must have
- Must have illustration of high level concept, and each Crop, Process and Product. The design should represent KVG's company style. This can be understood, but our logo, website and videos. We are a Green technology company and should have this overall feel, but not granola.
Nice to have
- You could use our logo and or style elements of the logo as we have in our branding. The leaf, Sky/Ocean. See website. I will upload a low res version as well.
Should not have
- copyrighted illustrations.

```html
<!DOCTYPE html>
<html lang="en">
<head>
<meta charset="utf-8">
<title>Sustainable Energy Farm Process Flowchart</title>
<link href="https://fonts.googleapis.com/css2?family=Arimo:wght@400;700&display=swap" rel="stylesheet">
<style>
  :root {
    --canvas: #ffffff;
    --ink: #1a1a1a;
    --header-ink: #3b2a0c;
    --band-start: #ffffff;
    --band-end: #f3ad2c;
    --title-top: #3bbf2e;
    --title-bottom: #0a6311;
    --title-edge: #0c4a10;
    --tile-edge: #0f5fa8;
    --tile-top: #5fb2ec;
    --tile-bottom: #1c6cc0;
  }
  * { box-sizing: border-box; margin: 0; padding: 0; }
  html, body { width: 1200px; height: 900px; overflow: hidden; background: var(--canvas); }
  body { font-family: "Arimo", Arial, sans-serif; color: var(--ink); }

  .flowchart { position: relative; width: 1200px; height: 900px; overflow: hidden; }

  .column-band {
    position: absolute; left: 300px; top: 0; width: 900px; height: 58px;
    background: linear-gradient(90deg, var(--band-start) 0%, #fde7b8 35%, var(--band-end) 100%);
  }
  .column-heading {
    position: absolute; top: 14px; font-size: 23px; font-weight: 700;
    color: var(--header-ink); transform: translateX(-50%);
  }
  .column-heading.crops { left: 428px; }
  .column-heading.processes { left: 742px; }
  .column-heading.products { left: 1114px; }

  .title-panel {
    position: absolute; left: 16px; top: 38px; width: 194px; height: 218px;
    border-radius: 18px; border: 3px solid var(--title-edge);
    background: linear-gradient(180deg, var(--title-top), var(--title-bottom));
    display: flex; align-items: center; justify-content: center; text-align: center;
    color: #fff; font-size: 27px; font-weight: 700; line-height: 1.18;
    text-shadow: 0 0 2px #063b0a, 0 0 2px #063b0a;
  }

  .region-map {
    position: absolute; left: 0; top: 420px; width: 150px; height: 160px;
    border-radius: 40% 60% 50% 45%;
    background: radial-gradient(circle at 50% 50%, #3ec43a, #138a1c);
  }

  .connectors { position: absolute; left: 0; top: 0; width: 1200px; height: 900px; }

  .node { position: absolute; text-align: center; }
  .node-tile {
    display: block; margin: 0 auto; border-radius: 16px;
    border: 3px solid var(--tile-edge);
    box-shadow: 0 2px 4px rgba(0,0,0,.35), inset 0 0 0 3px rgba(255,255,255,.55);
    background: linear-gradient(180deg, var(--tile-top), var(--tile-bottom));
  }
  .node-label {
    display: block; margin-top: 6px; font-size: 16px; font-weight: 700; white-space: nowrap;
  }
  .node-label.wide { margin-left: -40px; margin-right: -40px; }

  .crop { left: 366px; width: 124px; }
  .crop .node-tile { width: 124px; height: 124px; }
  .crop.solar .node-tile { background: linear-gradient(180deg, #f7d23a 0%, #f08a1c 45%, #1b4fa6 100%); }
  .crop.jatropha .node-tile { background: linear-gradient(180deg, #5fb2ec, #1c6cc0); }
  .crop.cash .node-tile { background: linear-gradient(180deg, #f2a23a 0%, #4d9ee0 55%, #1c6cc0 100%); }

  .process { left: 678px; width: 128px; }
  .process .node-tile { width: 108px; height: 108px; }
  .process.methane .node-tile { background: linear-gradient(180deg, #5fb2ec 0%, #1c6cc0 60%, #f2cf1f 100%); }
  .process.digester .node-tile { background: linear-gradient(180deg, #f3e3d0 0%, #5fb2ec 45%, #4a2d17 100%); }
  .process.extraction .node-tile { background: linear-gradient(180deg, #5fb2ec 0%, #1f1f1f 55%, #c9d2dc 100%); }
  .process.refinery .node-tile { background: linear-gradient(180deg, #5fb2ec 0%, #c8ccd2 40%, #7a818a 100%); }

  .product { left: 1050px; width: 128px; }
  .product .node-tile { width: 100px; height: 100px; }
  .product.grid .node-tile { background: linear-gradient(180deg, #dff0fb, #6fb5e6); }
  .product.fertilizer .node-tile { background: linear-gradient(180deg, #9fd86a 0%, #2a2a2a 70%, #5fb2ec 100%); }
  .product.crude-oil .node-tile { background: linear-gradient(180deg, #eff3ec 0%, #d8dcd6 60%, #5fb2ec 100%); }
  .product.biofuel .node-tile { background: linear-gradient(180deg, #8ed15a 0%, #3c9a2e 60%, #1c6cc0 100%); }
  .product.squash .node-tile { background: linear-gradient(180deg, #5fb2ec 0%, #e7a24a 45%, #b86a1c 100%); }
</style>
</head>
<body>
<main class="flowchart">
  <div class="column-band"></div>
  <div class="column-heading crops">Crops</div>
  <div class="column-heading processes">Processes</div>
  <div class="column-heading products">Products</div>

  <div class="title-panel">Sustainable<br>Energy<br>Farm<br>Process<br>Flowchart</div>

  <div class="region-map" role="img" aria-label="Map of Costa Rica with farm locations marked"></div>

  <svg class="connectors" viewBox="0 0 1200 900" aria-hidden="true">
    <defs>
      <linearGradient id="flowH" gradientUnits="userSpaceOnUse" x1="150" y1="0" x2="1060" y2="0">
        <stop offset="0" stop-color="#1f9a19"/>
        <stop offset="1" stop-color="#7fe04a"/>
      </linearGradient>
      <linearGradient id="flowV" gradientUnits="userSpaceOnUse" x1="0" y1="540" x2="0" y2="140">
        <stop offset="0" stop-color="#1f9a19"/>
        <stop offset="1" stop-color="#7fe04a"/>
      </linearGradient>
      <marker id="head" viewBox="0 0 10 10" refX="1" refY="5" markerWidth="3" markerHeight="3" orient="auto">
        <path d="M0,0 L10,5 L0,10 Z" fill="#3cba2c"/>
      </marker>
    </defs>
    <g fill="none" stroke-width="14" stroke-linecap="butt" marker-end="url(#head)">
      <path d="M150,536 H200 C250,536 255,142 322,142" stroke="url(#flowV)"/>
      <path d="M150,536 H322" stroke="url(#flowH)"/>
      <path d="M150,536 H200 C250,536 255,804 322,804" stroke="url(#flowH)"/>
      <path d="M500,86 H950 C990,86 995,130 1020,130" stroke="url(#flowH)"/>
      <path d="M830,190 H1020" stroke="url(#flowH)"/>
      <path d="M500,536 H640" stroke="url(#flowH)"/>
      <path d="M830,376 H1020" stroke="url(#flowH)"/>
      <path d="M830,536 H1020" stroke="url(#flowH)"/>
      <path d="M830,690 H1020" stroke="url(#flowH)"/>
      <path d="M500,880 H930 C975,880 985,818 1020,818" stroke="url(#flowH)"/>
    </g>
    <g fill="none" stroke-width="12" stroke="#2da424" marker-end="url(#head)">
      <path d="M742,518 V500"/>
      <path d="M742,324 V300"/>
      <path d="M742,662 V696"/>
    </g>
  </svg>

  <div class="node crop solar" style="top:76px">
    <span class="node-tile" role="img" aria-label="Sun shining over solar panels"></span>
    <span class="node-label">Solar</span>
  </div>
  <div class="node crop jatropha" style="top:472px">
    <span class="node-tile" role="img" aria-label="Jatropha plant silhouette"></span>
    <span class="node-label wide">Jatropha Cultivation</span>
  </div>
  <div class="node crop cash" style="top:742px">
    <span class="node-tile" role="img" aria-label="Dollar coin rising over planted field rows"></span>
    <span class="node-label">Cash Crops</span>
  </div>

  <div class="node process methane" style="top:124px">
    <span class="node-tile" role="img" aria-label="Methane generator with lightning bolt"></span>
    <span class="node-label wide">Methane Generator</span>
  </div>
  <div class="node process digester" style="top:330px">
    <span class="node-tile" role="img" aria-label="Domed anaerobic digester tank"></span>
    <span class="node-label wide">Seedcake Anaerobic Digester</span>
  </div>
  <div class="node process extraction" style="top:524px">
    <span class="node-tile" role="img" aria-label="Jatropha seeds dripping oil"></span>
    <span class="node-label wide">Oil Extraction and Filtration</span>
  </div>
  <div class="node process refinery" style="top:734px">
    <span class="node-tile" role="img" aria-label="Refinery silo"></span>
    <span class="node-label">Refinery</span>
  </div>

  <div class="node product grid" style="top:96px">
    <span class="node-tile" role="img" aria-label="Electric transmission towers"></span>
    <span class="node-label">Electric Grid</span>
  </div>
  <div class="node product fertilizer" style="top:292px">
    <span class="node-tile" role="img" aria-label="Pile of organic fertilizer with leaves"></span>
    <span class="node-label wide">Organic Fertilizer</span>
  </div>
  <div class="node product crude-oil" style="top:452px">
    <span class="node-tile" role="img" aria-label="Storage tank of jatropha crude oil"></span>
    <span class="node-label wide">Jatropha Crude Oil</span>
  </div>
  <div class="node product biofuel" style="top:608px">
    <span class="node-tile" role="img" aria-label="Fuel pump with green leaf"></span>
    <span class="node-label">Biofuel</span>
  </div>
  <div class="node product squash" style="top:768px">
    <span class="node-tile" role="img" aria-label="Butternut squash"></span>
    <span class="node-label">Squash</span>
  </div>
</main>
</body>
</html>
```